Promotional Double-Sided postcard

We are promoting a web cam studio (www.velmorastudio.com) and making a postcard for recruiting models. I have attached a .doc of a very basic 8.5x11 flyer we drew up which contains the same information we want conveyed in the postcard. I've also attached our website's logo.

Industry/Entity Type

Promotional

```html
<!DOCTYPE html>
<html lang="en">
<head>
<meta charset="utf-8">
<title>Velmora Studio – Model Recruiting Postcard</title>
<link rel="stylesheet" href="https://fonts.googleapis.com/css2?family=Archivo+Black&family=Arimo:wght@400;700&display=swap">
<style>
  :root {
    --magenta: #d41a7c;
    --magenta-deep: #9c1462;
    --plum: #3b0a2c;
    --pink-soft: #e0609f;
    --pink-bar: #ec1f86;
    --white: #ffffff;
    --ink: #222222;
    --frame: #c2456f;
  }
  * { margin: 0; padding: 0; box-sizing: border-box; }
  html, body { width: 757px; height: 1200px; overflow: hidden; background: var(--white); }
  body { position: relative; font-family: "Arimo", Arial, sans-serif; }

  .card { position: absolute; left: 0; width: 757px; overflow: hidden; }
  .card--front { top: 0; height: 582px; }
  .card--back { top: 618px; height: 581px; border: 1px solid var(--frame); }

  .front-photo {
    position: absolute; inset: 0;
    background:
      radial-gradient(ellipse 120px 260px at 575px 300px, rgba(200,30,60,0.85), rgba(200,30,60,0) 70%),
      radial-gradient(ellipse 500px 260px at 380px 60px, rgba(220,40,150,0.9), rgba(220,40,150,0) 75%),
      linear-gradient(180deg, #c21a83 0%, #8a1667 38%, #4a0d38 70%, var(--plum) 100%);
  }
  .brand {
    position: absolute; display: flex; align-items: center; gap: 8px;
    color: var(--white); font-family: "Arimo", Arial, sans-serif; font-weight: 700;
    font-size: 22px; letter-spacing: 0.5px;
  }
  .brand__dot { width: 16px; height: 16px; border-radius: 50%; background: var(--white); }
  .card--front .brand { left: 32px; top: 58px; }

  .headline {
    position: absolute; right: 389px; top: 178px; text-align: right; color: var(--white);
  }
  .headline__amount { font-family: "Archivo Black", sans-serif; font-size: 68px; font-style: italic; line-height: 1; letter-spacing: 1px; }
  .headline__period { font-family: "Arimo", Arial, sans-serif; font-weight: 700; font-size: 35px; line-height: 1; margin-top: 2px; }

  .pitch {
    position: absolute; left: 28px; top: 286px; width: 339px;
    color: var(--white); font-size: 15px; line-height: 22px; text-align: justify;
  }
  .offer {
    position: absolute; right: 32px; top: 283px; width: 320px;
    color: var(--white); font-weight: 700; font-size: 14px; line-height: 17.5px; text-align: right;
  }
  .perks {
    position: absolute; right: 50px; top: 366px; list-style: none;
    color: var(--white); font-weight: 700; font-size: 11px; line-height: 17px; text-align: right;
  }
  .perks-bar { position: absolute; left: 711px; top: 368px; width: 9px; height: 100px; background: var(--pink-bar); }

  .front-wave { position: absolute; left: 0; top: 460px; width: 757px; height: 122px; }
  .contact {
    position: absolute; left: 0; width: 396px; text-align: center;
    color: var(--white); font-weight: 700; font-size: 21px; letter-spacing: 0.6px;
  }
  .contact--web { top: 515px; }
  .contact--phone { top: 546px; }

  .back-photo {
    position: absolute; left: 0; top: 0; width: 368px; height: 581px;
    background:
      radial-gradient(ellipse 150px 220px at 150px 240px, rgba(240,90,170,0.55), rgba(240,90,170,0) 70%),
      linear-gradient(160deg, #e0419a 0%, var(--magenta) 45%, #b5156c 100%);
  }
  .back-band { position: absolute; left: 0; top: 522px; width: 368px; height: 59px; background: var(--magenta); }
  .card--back .brand { left: 0; width: 368px; justify-content: center; top: 330px; }
  .back-cta {
    position: absolute; left: 0; top: 409px; width: 368px; text-align: center;
    color: var(--white); font-weight: 700; font-size: 21px; line-height: 29.5px; letter-spacing: 0.6px;
  }

  .mail-side { position: absolute; left: 368px; top: 0; width: 388px; height: 579px; background: var(--white); color: var(--ink); }
  .mail-label { position: absolute; font-size: 21px; line-height: 27px; }
  .mail-label--postage { left: 248px; top: 70px; text-align: center; }
  .mail-label--address { left: 39px; top: 226px; }
  .mail-label--barcode { left: 48px; top: 517px; }
  .address-line { position: absolute; left: 41px; width: 307px; height: 1px; background: var(--ink); }
</style>
</head>
<body>

<section class="card card--front">
  <div class="front-photo" role="img" aria-label="Woman in a red gown posing before a crowd of photographers under magenta stage light"></div>

  <div class="brand"><span class="brand__dot"></span>Velmora</div>

  <div class="headline">
    <div class="headline__amount">$3000</div>
    <div class="headline__period">every month</div>
  </div>

  <p class="pitch">That is a realistic number you can earn average working part-time as a live webcam model. Some full time models make that much in a WEEK, but think of what you could do with just an extra $3000 a month! If you’ve been given this flyer, it’s because YOU could be making great money as a live webcam model.</p>

  <p class="offer">From the comfort of your home or in our Beverly Hills cam studio,<br>we will help you discover one of the most lucrative yet flexible jobs there is.</p>

  <ul class="perks">
    <li>* Free photo shoots for all models.</li>
    <li>* Artistic freedom.&nbsp; Nudity is entirely up to you.</li>
    <li>* Block anyone in Los Angeles</li>
    <li>from ever seeing you online.</li>
    <li>* Friendly staff with studio access</li>
    <li>available 24 hours a day, 7 days a week</li>
  </ul>
  <div class="perks-bar"></div>

  <svg class="front-wave" viewBox="0 0 757 122" preserveAspectRatio="none" aria-hidden="true">
    <path d="M0 44 C120 -10 230 10 340 42 C470 80 620 80 757 48 L757 122 L0 122 Z" fill="var(--pink-soft)"/>
    <path d="M0 66 C110 20 220 28 330 55 C470 92 630 96 757 62 L757 122 L0 122 Z" fill="var(--magenta)"/>
  </svg>

  <div class="contact contact--web">www.velmorastudio.com</div>
  <div class="contact contact--phone">Call 18005550142</div>
</section>

<section class="card card--back">
  <div class="back-photo" role="img" aria-label="Portrait of a young woman with long wavy hair, tinted magenta"></div>
  <div class="back-band"></div>

  <div class="brand"><span class="brand__dot"></span>Velmora</div>

  <p class="back-cta">Visit our website at<br>www.velmorastudio.com<br>to contact us with<br>any questions.<br>or Call 18005550142</p>

  <div class="mail-side">
    <div class="mail-label mail-label--postage">Postage<br>Area</div>
    <div class="mail-label mail-label--address">AddressArea</div>
    <div class="address-line" style="top:294px"></div>
    <div class="address-line" style="top:325px"></div>
    <div class="address-line" style="top:357px"></div>
    <div class="address-line" style="top:388px"></div>
    <div class="mail-label mail-label--barcode">Barcode Area</div>
  </div>
</section>

</body>
</html>
```